Christmas social media advert post

I am looking for an eye catching advert for use mainly on social media posts.
The following is the detail of the event.

Christmas special offer-
£10pp,– offer includes –
Half an hour Toboggan track,
Half an hour Slingshot paintballs (20 paintballs pp) and safe target archery (under cover and indoor ranges). Activities all the family from age 4 to grandparents can join in,
Also available – Add on indoor activities including Mini Curling, Bead Blitz, Safe axe throwing, Air juggler – from £3.50pp and age 6plus
Café open for hot food and drinks in the ‘Fireside Frost Lodge and the heated Christmas marquee.

A basic idea I put together for what I feel is the important information is -

Christmas Special offer -
Starts Saturday 20th December.
£10pp – offer includes –
Half an hour Slingshot paintballs (20 paintballs pp) and safe target archery (under cover and indoor ranges). Activities all the family from age 4 to grandparents can join in. Booking is essential - details on how below.
Also available Add on indoor activities - including Mini Curling, Bead Blitz, Safe axe throwing, Air juggler – from £3.50pp and age 6plus.
Ages start from 4 plus.
All activities are great for children and adults so perfect for families as well as friends, parties and get togethers.
Free huge car parks,
Booking is easy-
Just Message from messenger (on this post) or email
martin@hollowbrookleisurepark.co.uk for availability of your preferred date and time.

I would be happy to send the detailed information to enquiries if it meant a better looking advert / post.

Full details are in the picture uploads, feel free to use as much or as little of the information as you feel best.

```html
<!DOCTYPE html>
<html lang="en">
<head>
<meta charset="utf-8">
<title>Christmas Special Offer</title>
<link href="https://fonts.googleapis.com/css2?family=Great+Vibes&family=Fraunces:opsz,wght@9..144,600;9..144,700;9..144,800&family=Outfit:wght@300;400;500&display=swap" rel="stylesheet">
<style>
  :root {
    --green: #1d5538;
    --green-deep: #184a30;
    --green-ink: #1f5a3a;
    --cream: #f3e6cf;
    --ticket: #f5e7d3;
    --red: #e8473a;
    --gold: #e2bf85;
    --ink: #3a3a3a;
  }
  * { margin: 0; padding: 0; box-sizing: border-box; }
  html, body { width: 1200px; height: 1200px; overflow: hidden; }
  body { background: var(--green); font-family: "Outfit", sans-serif; }
  .advert { position: relative; width: 1200px; height: 1200px; overflow: hidden;
    background: linear-gradient(180deg, #2a6446 0%, var(--green) 45%, var(--green-deep) 100%); }
  .abs { position: absolute; line-height: 1; white-space: nowrap; }
  .photo-range { position: absolute; left: 0; top: 0; width: 720px; height: 900px;
    background: radial-gradient(ellipse at 10% 8%, rgba(230,220,170,.55) 0%, rgba(90,130,100,.35) 30%, rgba(29,85,56,0) 70%),
                linear-gradient(180deg, #3f7257 0%, #2c6347 50%, rgba(29,85,56,0) 100%); }
  .tree { position: absolute; left: 0; top: 70px; width: 96px; height: 250px;
    background: radial-gradient(ellipse at 40% 50%, #8fa862 0%, #5f7f44 60%, rgba(60,100,60,0) 100%); border-radius: 0 60% 60% 0; }
  .gift { position: absolute; background: linear-gradient(135deg, #e43a3a, #b81f28); border-radius: 8px; transform: rotate(45deg); }
  .gift-left { left: 10px; top: 238px; width: 78px; height: 78px; }
  .gift-right { left: 1060px; top: 755px; width: 220px; height: 220px; border-radius: 18px; }
  .santa-hat { position: absolute; left: 472px; top: 490px; width: 166px; height: 118px;
    background: radial-gradient(ellipse at 40% 40%, #e23a2c 0%, #c0201e 60%, rgba(192,32,30,0) 72%); }
  .flake { position: absolute; width: 34px; height: 34px; border-radius: 50%;
    background: radial-gradient(circle, rgba(226,191,133,.9) 0%, rgba(226,191,133,.25) 55%, rgba(226,191,133,0) 70%); }
  .title-script { left: 100px; top: 120px; font-family: "Great Vibes", cursive; font-size: 150px; color: var(--cream); }
  .title-serif { left: 165px; font-family: "Fraunces", serif; font-weight: 800; font-size: 112px; color: var(--red);
    letter-spacing: -2px; text-shadow: 4px 5px 0 rgba(80,20,20,.45); }
  .date-box { position: absolute; left: 85px; top: 578px; width: 475px; height: 163px;
    border: 1.5px solid rgba(243,230,207,.55); border-radius: 10px; background: var(--green-deep); }
  .date-box .starts { left: 44px; top: 55px; font-family: "Fraunces", serif; font-weight: 700; font-size: 50px; color: var(--cream); }
  .date-box .divider { position: absolute; left: 209px; top: 33px; width: 1.5px; height: 98px; background: rgba(243,230,207,.7); }
  .date-box .day { left: 227px; top: 30px; font-family: "Fraunces", serif; font-weight: 700; font-size: 54px; color: var(--cream); }
  .date-box .day sup { font-size: 28px; vertical-align: 22px; }
  .date-box .weekday { left: 228px; top: 92px; font-size: 43px; font-weight: 300; color: var(--cream); }
  .feature-icon { position: absolute; left: 85px; width: 42px; height: 42px; }
  .feature-title { left: 147px; font-family: "Fraunces", serif; font-weight: 700; font-size: 33px; color: var(--cream); }
  .feature-text { position: absolute; left: 85px; width: 560px; font-size: 25px; line-height: 34px; color: var(--cream); font-weight: 300; }
  .ticket { position: absolute; left: 690px; top: 101px; width: 450px; height: 835px; }
  .centre { left: 690px; width: 450px; text-align: center; }
  .price { top: 218px; font-size: 33px; font-weight: 500; color: var(--ink); }
  .tagline { top: 266px; font-family: "Fraunces", serif; font-weight: 700; font-size: 29px; color: var(--green-ink); letter-spacing: -.5px; }
  .rule { position: absolute; left: 738px; top: 318px; width: 351px; height: 1.5px; background: #6b6b6b; }
  .included-title { top: 351px; font-family: "Fraunces", serif; font-weight: 700; font-size: 19px; color: var(--green-ink); }
  .list-item { left: 853px; font-size: 19px; font-weight: 300; color: var(--ink); }
  .list-icon { position: absolute; left: 823px; width: 22px; height: 20px; }
  .suits { top: 523px; font-size: 25px; color: var(--green-ink); line-height: 33px; white-space: normal; }
  .addon-title { top: 676px; font-family: "Fraunces", serif; font-weight: 700; font-size: 21px; color: var(--green-ink); }
  .addon-price { top: 713px; font-size: 33px; font-weight: 400; color: var(--ink); }
  .addon-list { font-size: 18px; font-weight: 300; color: var(--ink); }
  .tick { color: var(--green-ink); font-weight: 500; }
  .booking { left: 690px; width: 450px; text-align: center; }
  .booking-title { top: 977px; font-family: "Fraunces", serif; font-weight: 700; font-size: 34px; color: var(--cream); }
  .booking-text { top: 1030px; font-size: 25px; font-weight: 300; color: var(--cream); }
  .booking-or { top: 1071px; font-family: "Fraunces", serif; font-weight: 800; font-size: 31px; color: var(--red); }
  .email { left: 728px; top: 1122px; font-size: 19.5px; font-weight: 300; color: var(--cream); }
  .email-icon { position: absolute; left: 690px; top: 1124px; width: 28px; height: 20px; }
</style>
</head>
<body>
<main class="advert">
  <div class="photo-range" role="img" aria-label="Archer drawing a bow towards a target in a covered archery range"></div>
  <div class="tree" role="img" aria-label="Sunlit Christmas tree branches"></div>
  <div class="gift gift-left" role="img" aria-label="Red gift box with gold bow"></div>

  <div class="abs title-script">Christmas</div>
  <div class="abs title-serif" style="top:272px">Special</div>
  <div class="abs title-serif" style="top:398px">Offer</div>

  <div class="flake" role="img" aria-label="Gold snowflake" style="left:82px;top:474px"></div>

  <section class="date-box">
    <div class="abs starts">Starts</div>
    <div class="divider"></div>
    <div class="abs day">20<sup>th</sup> Dec</div>
    <div class="abs weekday">Saturday</div>
  </section>
  <div class="santa-hat" role="img" aria-label="Red and white Santa hat"></div>

  <div class="flake" role="img" aria-label="Gold snowflake" style="left:570px;top:780px"></div>

  <svg class="feature-icon" style="top:810px" viewBox="0 0 42 42" fill="none" stroke="#f3e6cf" stroke-width="2">
    <path d="M6 4h30"/><circle cx="21" cy="24" r="16"/><circle cx="21" cy="24" r="11"/>
    <path d="M14 22h12v4a5 5 0 0 1-5 5h-2a5 5 0 0 1-5-5z"/><path d="M26 23h2a2 2 0 0 1 0 4h-2"/>
  </svg>
  <div class="abs feature-title" style="top:829px">Café Open</div>
  <p class="feature-text" style="top:863px">Enjoy hot food &amp; drinks in the Fireside Frost Lodge and heated Christmas marquee.</p>

  <svg class="feature-icon" style="top:978px" viewBox="0 0 42 42" fill="none" stroke="#f3e6cf" stroke-width="2">
    <path d="M14 30C8 23 4 18 4 13a10 10 0 0 1 20 0"/><path d="M11 18v-9h4a3 3 0 0 1 0 6h-4"/>
    <rect x="19" y="26" width="20" height="10" rx="3"/><path d="M21 26l3-6h10l3 6"/><circle cx="24" cy="31" r="1.3"/><circle cx="34" cy="31" r="1.3"/>
  </svg>
  <div class="abs feature-title" style="top:982px">Free large car parks</div>
  <p class="feature-text" style="top:1028px">Ideal for families, friends, parties &amp; festive get-togethers.</p>

  <div class="flake" role="img" aria-label="Gold snowflake" style="left:387px;top:1106px"></div>

  <svg class="ticket" viewBox="0 0 450 835">
    <path fill="#f5e7d3" d="M0 0H450V835H0Z"/>
    <g fill="#1d5538">
      <circle cx="25" cy="0" r="14"/><circle cx="79" cy="0" r="14"/><circle cx="133" cy="0" r="14"/><circle cx="187" cy="0" r="14"/>
      <circle cx="241" cy="0" r="14"/><circle cx="295" cy="0" r="14"/><circle cx="349" cy="0" r="14"/><circle cx="403" cy="0" r="14"/>
    </g>
    <g fill="#1a4f33">
      <circle cx="25" cy="835" r="14"/><circle cx="79" cy="835" r="14"/><circle cx="133" cy="835" r="14"/><circle cx="187" cy="835" r="14"/>
      <circle cx="241" cy="835" r="14"/><circle cx="295" cy="835" r="14"/><circle cx="349" cy="835" r="14"/><circle cx="403" cy="835" r="14"/>
    </g>
    <g stroke="#1f5a3a" fill="#1f5a3a">
      <path d="M52 529H300" stroke-width="2"/><path d="M302 529H395" stroke-width="2"/>
      <path d="M223 524l4 5-4 5-4-5z"/><circle cx="210" cy="529" r="1.8"/><circle cx="236" cy="529" r="1.8"/>
    </g>
  </svg>
  <div class="flake" role="img" aria-label="Gold snowflake" style="left:1052px;top:220px"></div>

  <div class="abs centre price">£10 per person</div>
  <div class="abs centre tagline">Family Fun for All Ages!</div>
  <div class="rule"></div>
  <div class="abs centre included-title">What’s Included?</div>

  <svg class="list-icon" style="top:383px" viewBox="0 0 22 20" fill="none" stroke="#1f5a3a" stroke-width="1.4"><path d="M1 18h20M2 18V8l4-4 3 5 4-6 3 5 4-2v12M6 18v-7M11 18v-6M16 18v-7"/></svg>
  <div class="abs list-item" style="top:383px">30 mins Toboggan Track</div>
  <svg class="list-icon" style="top:410px" viewBox="0 0 22 20" fill="none" stroke="#1f5a3a" stroke-width="1.4"><path d="M6 2l5 8 5-8M11 10v9"/><path d="M4 4h4M14 4h4"/></svg>
  <div class="abs list-item" style="top:410px">30 mins Slingshot Paintballs</div>
  <div class="abs list-item" style="top:431px">(20 paintballs pp)</div>
  <svg class="list-icon" style="top:459px" viewBox="0 0 22 20" fill="none" stroke="#1f5a3a" stroke-width="1.4"><circle cx="13" cy="11" r="8"/><circle cx="13" cy="11" r="4.5"/><circle cx="13" cy="11" r="1.2"/><path d="M1 3l12 8M1 3h3M1 3v3"/></svg>
  <div class="abs list-item" style="top:459px">Safe Target Archery (indoor</div>
  <div class="abs list-item" style="top:480px">&amp; under cover)</div>

  <div class="abs centre suits">Perfect for everyone aged 4+<br>from kids to grandparents!</div>

  <div class="abs centre addon-title">Optional Add-On Indoor Activities</div>
  <div class="abs centre addon-price">(from £3.50pp | ages 6+)</div>
  <div class="abs centre addon-list" style="top:776px"><span class="tick">✓</span> Mini Curling &nbsp;| &nbsp;<span class="tick">✓</span> Bead Blitz</div>
  <div class="abs centre addon-list" style="top:804px"><span class="tick">✓</span> Safe Axe Throwing &nbsp;| &nbsp;<span class="tick">✓</span> Air Juggler</div>

  <div class="gift gift-right" role="img" aria-label="Red gift box with gold ribbon bow"></div>

  <div class="abs booking booking-title">Booking Essential</div>
  <div class="abs booking booking-text">Message us on Chatterly</div>
  <div class="abs booking booking-or">OR</div>
  <svg class="email-icon" viewBox="0 0 28 20" fill="none" stroke="#f3e6cf" stroke-width="1.8"><rect x="1" y="1" width="26" height="18"/><path d="M1 1l13 10L27 1M1 19l10-9M27 19l-10-9"/></svg>
  <div class="abs email">martin@hollowbrookleisurepark.co.uk</div>
</main>
</body>
</html>
```